Etiketten für verschiedene Lebensmittel
Zielgruppe
Verkauf von Lebensmitteln über das Internet, direkt und über Lebensmittelautomaten
Aufgabenstellung
Es soll die Verbindung zur Landwirtschaft behalten werden, das Etikett soll eine Fusion von Tradition und Professionalität darstellen.
Das Logo ist vorhanden, wird angehängt. (Logo.png)
Das Logo für die Automaten ist nur sekundär, habe es aber auch angehängt (frischkastenlogo.jpg)
Die (noch nicht fertige) Homepage ist hier:
http://landwirtschaft.brennhofer.at/
Der Umfang wird erweitert, brauchen mehrere Etiketten mit der selben Richtung.
Wir starten mit Fleisch, dann wird bei erfolgreicher Zusammenarbeit auf mehrere andere erweitert, unter anderem andere Fleischsorten, Öl und Hanfmehlprodukte.
Das Preisgeld wird mit diesen weiteren Projekten natürlich auch erweitert.
Mehr Informationen für das Fleischetikett:
Das Etikett wird auf vakuumverpacktes Fleisch geklebt.
Vom Format sind wir flexibel, beim Fleisch soll es aber eher in Richtung Quadratisch gehen (ist aber nicht zwingend).
Informationen auf dem Etikett sind:
- Fleischsorte: (Schnitzel, Kotlett, Speck, Braten usw.) --> sollte leicht austauschbar sein, da wir das Etikett für alle Fleischsorten nutzen wollen.
- Inhaltsstoffe: Die Inhaltsstoffe sind sehr wenige, da es sich um rohes Fleisch handelt, bei marinierten Produkten und dem Speck brauchen wir diese jedoch.
- Ablaufdatum und Füllmenge: Diese zwei informationen werden dann beim Druck erst geliefert, geplant ist ein Programm das die Informationen direkt vor dem Druck aktualisiert
- Größe des Etikettes: 8-12cm Durchmesser, grob geschätzt, wir sind da auch flexibel da wir die Etiketten selbst drucken
- Das frischkasten Logo soll nicht eingebaut werden in diesem Etikett, werde das entfernen vom Anhang um Missverständnisse zu vermeiden
- Es handelt sich um Bio Schweinefleisch (hatte vergessen das anzumerken)
Habe das Brennhofer Logo auf eine bessere Auflösung geupdated
Auch andere kleinere Designs werden benötigt, wir freuen uns auf eine ..

```html
<!DOCTYPE html>
<html lang="de">
<head>
<meta charset="utf-8">
<title>Biohof Brennhofer – Etiketten Bio Kotelett</title>
<link rel="stylesheet" href="https://fonts.googleapis.com/css2?family=Source+Sans+3:ital,wght@0,700;1,400&family=Mulish:ital,wght@0,700;1,400&display=swap">
<style>
  :root {
    --backdrop: #d9d9d9;
    --forest: #0a2300;
    --cream: #f7e4b2;
    --cream-title: #f6dfa2;
    --olive: #8f9f5e;
    --ink: #0a2300;
    --wood-light: #d39a5c;
    --wood-dark: #8a5a32;
  }
  * { margin: 0; padding: 0; box-sizing: border-box; }
  html, body {
    width: 1200px; height: 720px; overflow: hidden;
    background: var(--backdrop);
  }
  .sheet { position: relative; width: 1200px; height: 720px; }
  .label {
    position: absolute; top: 98px;
    width: 519px; height: 519px;
    background: var(--forest);
    overflow: hidden;
  }
  .label--marinated { left: 65px; }
  .label--plain { left: 612px; }

  .brand {
    position: absolute; top: 78px; left: 0; width: 100%;
    text-align: center;
    font-family: "Source Sans 3", sans-serif;
    font-weight: 700;
    font-size: 40px;
    letter-spacing: 1px;
    color: var(--olive);
  }

  .food-band { position: absolute; left: 0; top: 0; width: 519px; height: 519px; }

  .product-name {
    position: absolute; left: 0; width: 100%;
    text-align: center;
    font-family: "Source Sans 3", sans-serif;
    color: var(--cream-title);
  }
  .product-name__title {
    position: absolute; left: 0; width: 100%; top: 368px;
    font-weight: 700; font-size: 37px; line-height: 1;
  }
  .product-name__variant {
    position: absolute; left: 0; width: 100%; top: 406px;
    font-style: italic; font-weight: 400; font-size: 23px; line-height: 1;
  }

  .info-strip {
    position: absolute; left: 0; bottom: 0;
    width: 100%; height: 69px;
    background: var(--cream);
    font-family: "Mulish", sans-serif;
    color: var(--ink);
    padding: 0 27px 0 30px;
  }
  .info-strip__row {
    display: flex; justify-content: space-between; align-items: baseline;
    margin-top: 16px;
    font-size: 15px; font-style: italic;
  }
  .info-strip__value { font-style: normal; font-weight: 700; font-size: 16px; }
  .info-strip__ingredients {
    margin-top: 5px;
    font-size: 11px; font-style: italic;
  }
</style>
</head>
<body>
<div class="sheet">

  <section class="label label--marinated">
    <div class="brand">Biohof Brennhofer</div>
    <svg class="food-band" viewBox="0 0 519 519" xmlns="http://www.w3.org/2000/svg">
      <defs>
        <linearGradient id="dishTonesA" x1="0" y1="0" x2="1" y2="1">
          <stop offset="0" stop-color="#c98a4f"/>
          <stop offset="0.45" stop-color="#d8b08a"/>
          <stop offset="0.8" stop-color="#b07a4c"/>
          <stop offset="1" stop-color="#5f7a36"/>
        </linearGradient>
      </defs>
      <g role="img" aria-label="Foto: gegrillte Bio-Koteletts auf Holzbrett mit Kartoffeln, Tomaten, Brokkoli und rotem Pfeffer">
        <path d="M0 222 C70 185 140 170 206 180 C280 192 320 225 371 222 C430 218 490 200 519 181 L519 319 C470 350 440 362 420 360 C330 352 220 300 128 319 C70 330 30 345 0 360 Z" fill="url(#dishTonesA)"/>
      </g>
      <path d="M0 222 C70 185 140 170 206 180 C280 192 320 225 371 222 C430 218 490 200 519 181" fill="none" stroke="var(--cream)" stroke-width="4"/>
      <path d="M519 319 C470 350 440 362 420 360 C330 352 220 300 128 319 C70 330 30 345 0 360" fill="none" stroke="var(--cream)" stroke-width="4"/>
    </svg>
    <div class="product-name">
      <div class="product-name__title">Bio Kotelett</div>
      <div class="product-name__variant">mariniert</div>
    </div>
    <div class="info-strip">
      <div class="info-strip__row">
        <span>Füllmenge <span class="info-strip__value">300 g</span></span>
        <span>Ablaufdatum <span class="info-strip__value">06.05.2017</span></span>
      </div>
      <div class="info-strip__ingredients">Zutaten: Meersalz, Knoblauch, Paprika, Rosmarin, grüner Pfeffer</div>
    </div>
  </section>

  <section class="label label--plain">
    <div class="brand">Biohof Brennhofer</div>
    <svg class="food-band" viewBox="0 0 519 519" xmlns="http://www.w3.org/2000/svg">
      <defs>
        <linearGradient id="dishTonesB" x1="0" y1="0" x2="1" y2="1">
          <stop offset="0" stop-color="#c98a4f"/>
          <stop offset="0.45" stop-color="#d8b08a"/>
          <stop offset="0.8" stop-color="#b07a4c"/>
          <stop offset="1" stop-color="#5f7a36"/>
        </linearGradient>
      </defs>
      <g role="img" aria-label="Foto: gegrillte Bio-Koteletts auf Holzbrett mit Kartoffeln, Tomaten, Brokkoli und rotem Pfeffer">
        <path d="M0 222 C70 185 140 170 206 180 C280 192 320 225 371 222 C430 218 490 200 519 181 L519 319 C470 350 440 362 420 360 C330 352 220 300 128 319 C70 330 30 345 0 360 Z" fill="url(#dishTonesB)"/>
      </g>
      <path d="M0 222 C70 185 140 170 206 180 C280 192 320 225 371 222 C430 218 490 200 519 181" fill="none" stroke="var(--cream)" stroke-width="4"/>
      <path d="M519 319 C470 350 440 362 420 360 C330 352 220 300 128 319 C70 330 30 345 0 360" fill="none" stroke="var(--cream)" stroke-width="4"/>
    </svg>
    <div class="product-name">
      <div class="product-name__title">Bio Kotelett</div>
    </div>
    <div class="info-strip">
      <div class="info-strip__row">
        <span>Füllmenge <span class="info-strip__value">300 g</span></span>
        <span>Ablaufdatum <span class="info-strip__value">06.05.2017</span></span>
      </div>
    </div>
  </section>

</div>
</body>
</html>
```